Celebrate Weekends

Hi Doreen,

I'm looking to do another promo poster for my shop. Please use similar style as GLIMMERAMA poster

Title and description :

CELEBRATE WEEKEND
$10 PHO
ALL DAY SATURDAY & SUNDAY

Order your NOODLE RUN or Eat-In
Limited Time Only
...............................................................

* Must use these photos in the poster

Shop

```html
<!DOCTYPE html>
<html lang="en">
<head>
<meta charset="utf-8">
<title>Celebrate Weekends – $10 Pho</title>
<link rel="stylesheet" href="https://fonts.googleapis.com/css2?family=Anton&family=Kaushan+Script&family=Montserrat:wght@800&family=Mouse+Memoirs&display=swap">
<style>
  :root {
    --charcoal-top: #4a4a4d;
    --charcoal-bottom: #2c2c2e;
    --orange: #f39a1f;
    --orange-deep: #ef6d22;
    --amber: #f8b023;
    --white: #ffffff;
    --ribbon-light: #27a6e3;
    --ribbon-dark: #1d3f98;
    --broth: #8a4a1c;
    --greens: #4f7d2c;
  }
  html, body { margin: 0; padding: 0; overflow: hidden; background: var(--charcoal-bottom); }
  .poster {
    position: relative;
    width: 849px; height: 1200px;
    overflow: hidden;
    background: linear-gradient(180deg, var(--charcoal-top) 0%, var(--charcoal-bottom) 100%);
    font-family: "Montserrat", sans-serif;
  }
  .sun-curve { position: absolute; left: 0; top: 0; width: 849px; height: 1200px; }

  .brand {
    position: absolute; left: 358px; top: 54px;
    width: 130px; height: 130px;
    display: flex; align-items: center; justify-content: center;
  }
  .brand-ring { position: absolute; inset: 0; border: 2px solid var(--white); border-radius: 50%; }
  .brand-name {
    font-family: "Montserrat", sans-serif; font-weight: 800;
    font-size: 16px; letter-spacing: 1px; color: var(--orange);
  }

  .headline { margin: 0; font-weight: 400; }
  .headline-line {
    position: absolute; display: block; white-space: nowrap;
    font-family: "Kaushan Script", cursive;
    color: var(--orange); line-height: 1; font-size: 116px;
    transform: rotate(-7deg); transform-origin: left 80%;
    text-shadow: 0 4px 6px rgba(0,0,0,0.35);
  }
  .headline-line.line-one { left: 72px; top: 258px; }
  .headline-line.line-two { left: 60px; top: 374px; }

  .price-badge {
    position: absolute; left: 548px; top: 94px;
    width: 304px; height: 304px; border-radius: 50%;
    background: var(--white);
    display: flex; align-items: center; justify-content: center;
  }
  .price-badge-inner {
    width: 276px; height: 276px; border-radius: 50%;
    background: linear-gradient(180deg, var(--amber) 0%, var(--orange-deep) 100%);
    display: flex; flex-direction: column; align-items: center; justify-content: center;
    margin-left: -14px;
    font-family: "Anton", sans-serif; color: var(--white); line-height: 0.95;
  }
  .price-amount { font-size: 104px; }
  .price-item { font-size: 88px; }

  .schedule {
    position: absolute; left: 80px; top: 494px; margin: 0;
    font-family: "Montserrat", sans-serif; font-weight: 800;
    font-size: 32px; letter-spacing: 5px; color: var(--white);
    transform: rotate(-6.6deg); transform-origin: left center; white-space: nowrap;
  }

  .bowl {
    position: absolute; border-radius: 50%;
    border: 12px solid var(--white);
    box-shadow: 0 14px 18px rgba(0,0,0,0.35);
  }
  .bowl-chicken { left: 178px; top: 572px; width: 334px; height: 200px;
    background: radial-gradient(ellipse at 55% 45%, var(--greens) 0%, var(--broth) 70%); }
  .bowl-beef { left: 422px; top: 716px; width: 334px; height: 200px;
    background: radial-gradient(ellipse at 50% 45%, var(--greens) 0%, #7a4a22 72%); }
  .bowl-tofu { left: 112px; top: 816px; width: 334px; height: 210px;
    background: radial-gradient(ellipse at 50% 45%, #c9682a 0%, #9b4a1c 75%); }

  .dish-label {
    position: absolute; box-sizing: border-box;
    border: 3px dotted var(--white); border-radius: 6px;
    display: flex; flex-direction: column; align-items: center; justify-content: center;
    font-family: "Kaushan Script", cursive; line-height: 0.95;
  }
  .label-chicken { left: 468px; top: 542px; width: 190px; height: 114px; color: var(--orange); font-size: 40px; }
  .label-tofu { left: 58px; top: 738px; width: 116px; height: 122px; color: var(--white); font-size: 40px; }
  .label-beef { left: 688px; top: 900px; width: 112px; height: 144px; color: var(--white); font-size: 40px; }

  .offer-ribbon {
    position: absolute; left: 400px; top: 986px;
    width: 268px; height: 76px;
    background: linear-gradient(90deg, var(--ribbon-light) 0%, var(--ribbon-dark) 100%);
    transform: rotate(-8deg) skewX(-4deg);
    display: flex; align-items: center; justify-content: center;
    font-family: "Mouse Memoirs", sans-serif; color: var(--white);
    font-size: 38px; letter-spacing: 1px;
  }
  .call-to-action {
    position: absolute; left: 0; right: 0; top: 1090px; margin: 0;
    text-align: center; font-family: "Mouse Memoirs", sans-serif; font-weight: 400;
    font-size: 58px; color: var(--white); letter-spacing: 1px;
  }
</style>
</head>
<body>
<main class="poster">
  <svg class="sun-curve" viewBox="0 0 849 1200" aria-hidden="true">
    <defs>
      <linearGradient id="sunFill" x1="0" y1="1" x2="1" y2="0">
        <stop offset="0" stop-color="#f07a1b"/>
        <stop offset="1" stop-color="#f8ab23"/>
      </linearGradient>
    </defs>
    <path d="M0 1200 L0 1040 Q 330 850 849 826 L849 1200 Z" fill="url(#sunFill)"/>
  </svg>

  <div class="brand">
    <span class="brand-ring"></span>
    <span class="brand-name">NOODLE RUN</span>
  </div>

  <div class="price-badge">
    <div class="price-badge-inner">
      <span class="price-amount">$10</span>
      <span class="price-item">PHO</span>
    </div>
  </div>

  <h1 class="headline">
    <span class="headline-line line-one">Celebrate</span>
    <span class="headline-line line-two">Weekends</span>
  </h1>

  <p class="schedule">ALL DAY SATURDAY &amp; SUNDAY</p>

  <div class="bowl bowl-chicken" role="img" aria-label="Photo of a bowl of chicken pho with herbs and red onion"></div>
  <div class="bowl bowl-beef" role="img" aria-label="Photo of a bowl of beef pho with meatballs and herbs"></div>
  <div class="bowl bowl-tofu" role="img" aria-label="Photo of a bowl of tofu pho with fried tofu and carrot"></div>

  <div class="dish-label label-chicken"><span>Chicken</span><span>Pho</span></div>
  <div class="dish-label label-tofu"><span>Tofu</span><span>Pho</span></div>
  <div class="dish-label label-beef"><span>Beef</span><span>Pho</span></div>

  <div class="offer-ribbon">LIMITED TIME ONLY!</div>

  <p class="call-to-action">ORDER YOUR NOODLE RUN OR EAT-IN</p>
</main>
</body>
</html>
```